Business card design needed for Automotive Reconditioning business

I have a logo design i just cant decide on the best color or layout for the business card, I will upload all the files so you can see all colors schemes we are considering. I have other file formats if needed let me know.

Target Market(s)

automotive dealerships

Contact Information for Business Card

HERE are the Descriptions and info needed on the card:
Interior Repair: Leather carpet burns panels dash Deoderize
Dealer products and Vin Verify
( spot for name and cell number) My name is Norman Bexley phone 614 352-4180 Title COO www.QuorvalMotive.com

Font styles to use
Sans Serif
Other font styles liked:
• what ever you think looks best

Requirements
Must have
• Must be able to change the name and phone for employees

```html
<!DOCTYPE html>
<html lang="en">
<head>
<meta charset="utf-8">
<title>Quorval Motive – Business Card Colour Options</title>
<link rel="stylesheet" href="https://fonts.googleapis.com/css2?family=Source+Sans+3:wght@400;700&display=swap">
<style>
  :root {
    --backdrop: #c8d0d5;
    --green: #93c13b;
    --red: #e21e26;
    --blue: #0f529c;
    --ink-dark: #232323;
    --ink-grey: #555555;
    --card-light: #f1f1f1;
    --card-white: #ffffff;
    --card-black: #1c1a1a;
  }
  * { margin: 0; padding: 0; box-sizing: border-box; }
  html, body { width: 799px; height: 1200px; overflow: hidden; }
  body {
    background: var(--backdrop);
    font-family: "Source Sans 3", sans-serif;
    position: relative;
  }
  .card {
    position: absolute;
    left: 198px;
    width: 408px;
    height: 259px;
    border-radius: 11px;
    overflow: hidden;
  }
  .card--green { top: 126px; background: var(--card-light); color: var(--ink-dark); --accent: var(--green); --rule: var(--ink-grey); --bg: var(--card-light); --brand: var(--ink-dark); }
  .card--red   { top: 473px; background: var(--card-black); color: #ffffff; --accent: var(--red); --rule: var(--red); --bg: var(--card-black); --brand: #ffffff; }
  .card--blue  { top: 805px; background: var(--card-white); color: var(--blue); --accent: var(--blue); --rule: var(--red); --bg: var(--card-white); --brand: #ffffff; }

  .card__art { position: absolute; inset: 0; width: 100%; height: 100%; }
  .card__accent { fill: var(--accent); }
  .card__rule { stroke: var(--rule); }
  .card__wrench { fill: var(--rule); }
  .card__wrench-gap { fill: var(--bg); }

  .brand {
    position: absolute;
    left: 214px;
    top: 60px;
    width: 170px;
    text-align: center;
    font-weight: 700;
    font-size: 22px;
    letter-spacing: 0.5px;
    color: var(--brand);
    white-space: nowrap;
  }
  .holder__name {
    position: absolute;
    left: 38px;
    top: 131px;
    font-size: 16.5px;
    font-weight: 700;
    line-height: 1;
  }
  .holder__title {
    position: absolute;
    left: 38px;
    top: 154px;
    font-size: 13px;
    line-height: 1;
  }
  .contact {
    position: absolute;
    left: 38px;
    top: 197px;
    font-size: 14.5px;
    line-height: 19px;
  }
</style>
</head>
<body>

<section class="card card--green">
  <svg class="card__art" viewBox="0 0 510 324" aria-hidden="true">
    <defs>
      <linearGradient id="shade-light" x1="0" y1="0" x2="1" y2="1">
        <stop offset="0" stop-color="#f1f1f1" stop-opacity="0"/>
        <stop offset="1" stop-color="#8a8a8a"/>
      </linearGradient>
    </defs>
    <circle cx="382" cy="36" r="180" fill="url(#shade-light)"/>
    <circle class="card__accent" cx="398" cy="27" r="178"/>
    <line class="card__rule" x1="47" y1="231" x2="250" y2="231" stroke-width="3"/>
    <line class="card__rule" x1="250" y1="231" x2="466" y2="231" stroke-width="5"/>
    <circle class="card__wrench" cx="470" cy="231" r="9"/>
    <rect class="card__wrench-gap" x="472" y="227" width="10" height="8"/>
  </svg>
  <div class="brand">Quorval Motive</div>
  <div class="holder__name">Name Surname</div>
  <div class="holder__title">position</div>
  <div class="contact">Phone: 614 352-4180<br>www.QuorvalMotive.com</div>
</section>

<section class="card card--red">
  <svg class="card__art" viewBox="0 0 510 324" aria-hidden="true">
    <defs>
      <linearGradient id="shade-dark" x1="0" y1="0" x2="1" y2="1">
        <stop offset="0" stop-color="#1c1a1a" stop-opacity="0"/>
        <stop offset="1" stop-color="#8d8d8d"/>
      </linearGradient>
    </defs>
    <circle cx="382" cy="36" r="180" fill="url(#shade-dark)"/>
    <circle class="card__accent" cx="398" cy="27" r="178"/>
    <line class="card__rule" x1="47" y1="231" x2="250" y2="231" stroke-width="3"/>
    <line class="card__rule" x1="250" y1="231" x2="466" y2="231" stroke-width="5"/>
    <circle class="card__wrench" cx="470" cy="231" r="9"/>
    <rect class="card__wrench-gap" x="472" y="227" width="10" height="8"/>
  </svg>
  <div class="brand">Quorval Motive</div>
  <div class="holder__name">Name Surname</div>
  <div class="holder__title">position</div>
  <div class="contact">Phone: 614 352-4180<br>www.QuorvalMotive.com</div>
</section>

<section class="card card--blue">
  <svg class="card__art" viewBox="0 0 510 324" aria-hidden="true">
    <defs>
      <linearGradient id="shade-white" x1="0" y1="0" x2="1" y2="1">
        <stop offset="0" stop-color="#ffffff" stop-opacity="0"/>
        <stop offset="1" stop-color="#8a8a8a"/>
      </linearGradient>
    </defs>
    <circle cx="382" cy="36" r="180" fill="url(#shade-white)"/>
    <circle class="card__accent" cx="398" cy="27" r="178"/>
    <line class="card__rule" x1="47" y1="231" x2="250" y2="231" stroke-width="3"/>
    <line class="card__rule" x1="250" y1="231" x2="466" y2="231" stroke-width="5"/>
    <circle class="card__wrench" cx="470" cy="231" r="9"/>
    <rect class="card__wrench-gap" x="472" y="227" width="10" height="8"/>
  </svg>
  <div class="brand">Quorval Motive</div>
  <div class="holder__name">Name Surname</div>
  <div class="holder__title">position</div>
  <div class="contact">Phone: 614 352-4180<br>www.QuorvalMotive.com</div>
</section>

</body>
</html>
```